Building company buisness cards

We are looking for a sharp modern new look for our business cards.
We are a New Zealand based company that specialises in house and land packages.
We have attached a photo of the current logo and would like to see if it can be improved somehow if needed.
We are open to any colours but we have chosen green at this stage.
Feel free to change the font and make the logo smarter looking.
Play with the colours and see what looks best.

We want a card that looks so good know one will want to throw it away!

Target Market(s)

Home buyers

Industry/Entity Type

Building

Contact Information for Business Card

Dorian Keswick
0217392604
dkeswick@tidewellhomecraft.co.nz
tidewellhomecraft.co.nz

Font styles to use
Serif
Sans Serif

Colors

Designer to choose colors to be used in the design.

Requirements
Must have
• Logo and company name on one side, details on the other side
Nice to have
• Color codes for the original green are HEX #4a8028, RGB(74,128,40), CMYK(42,0,69,50)
• Round corners, Raised and/or spot UV

```html
<!DOCTYPE html>
<html lang="en">
<head>
<meta charset="utf-8">
<title>Tidewell Homecraft – Business Cards</title>
<link href="https://fonts.googleapis.com/css2?family=Questrial&display=swap" rel="stylesheet">
<style>
  :root {
    --brand-green: #4a8028;
    --paper: #f7f7f7;
    --ink-grey: #4a4a4a;
    --rule-light: rgba(255,255,255,0.45);
    --rule-green: rgba(74,128,40,0.45);
    --backdrop: #e6e3de;
  }
  * { box-sizing: border-box; margin: 0; padding: 0; }
  html, body {
    width: 1200px; height: 900px; overflow: hidden;
    background: var(--backdrop);
    font-family: "Questrial", "Century Gothic", sans-serif;
  }
  .canvas { position: relative; width: 1200px; height: 900px; }

  .card {
    position: absolute;
    width: 560px; height: 340px;
    border-radius: 10px;
    overflow: hidden;
    box-shadow: 0 10px 28px rgba(0,0,0,0.18);
  }

  /* Front */
  .card--front {
    left: 60px; top: 70px;
    background: var(--brand-green);
    color: #fff;
    display: flex; flex-direction: column; align-items: center;
  }
  .wordmark { text-align: center; line-height: 1; }
  .wordmark__top { display: block; font-size: 34px; letter-spacing: 0.5px; }
  .wordmark__bottom { display: block; font-size: 58px; letter-spacing: 0.5px; }
  .card--front .wordmark { margin-top: 88px; }
  .card--front .wordmark__rule {
    width: 100px; height: 1px; background: var(--rule-light); margin: 14px auto 0;
  }
  .card--front .web-line {
    margin-top: 52px;
    font-size: 18px; letter-spacing: 6px;
  }

  /* Back */
  .card--back {
    left: 580px; top: 480px;
    background: var(--paper);
  }
  .card--back .wordmark {
    position: absolute; left: 40px; top: 44px; width: 260px;
    color: var(--brand-green);
  }
  .card--back .wordmark__top { font-size: 26px; }
  .card--back .wordmark__bottom { font-size: 40px; }
  .card--back .wordmark__rule {
    width: 70px; height: 1px; background: var(--rule-green); margin: 10px auto 0;
  }
  .holder-name {
    position: absolute; left: 40px; top: 158px;
    font-size: 26px; color: var(--ink-grey);
  }
  .contact-band {
    position: absolute; left: 0; top: 200px; width: 100%; height: 104px;
    background: var(--brand-green);
    color: #fff;
    padding: 12px 0 0 40px;
    list-style: none;
  }
  .contact-band li {
    display: flex; align-items: center; gap: 14px;
    height: 28px; font-size: 18px; letter-spacing: 1px;
  }
  .contact-band li.phone { font-size: 22px; letter-spacing: 3px; }
  .contact-band svg { width: 20px; height: 20px; flex: none; }
  .tagline {
    position: absolute; left: 0; bottom: 8px; width: 100%;
    white-space: nowrap; overflow: hidden;
    font-size: 13px; letter-spacing: 1px; color: var(--brand-green);
    padding-left: 12px;
  }
</style>
</head>
<body>
<main class="canvas">

  <section class="card card--front" aria-label="Business card front">
    <div class="wordmark">
      <span class="wordmark__top">tidewell</span>
      <span class="wordmark__bottom">homecraft.</span>
      <div class="wordmark__rule"></div>
    </div>
    <p class="web-line">tidewellhomecraft.co.nz</p>
  </section>

  <section class="card card--back" aria-label="Business card back">
    <div class="wordmark">
      <span class="wordmark__top">tidewell</span>
      <span class="wordmark__bottom">homecraft.</span>
      <div class="wordmark__rule"></div>
    </div>
    <p class="holder-name">Dorian Keswick</p>
    <ul class="contact-band">
      <li class="phone">
        <svg viewBox="0 0 24 24" fill="none" stroke="#fff" stroke-width="1.8" stroke-linecap="round" stroke-linejoin="round"><path d="M5 3h4l2 5-2.5 1.5a11 11 0 0 0 6 6L16 13l5 2v4a2 2 0 0 1-2 2A16 16 0 0 1 3 5a2 2 0 0 1 2-2z"/></svg>
        0217392604
      </li>
      <li class="email">
        <svg viewBox="0 0 24 24" fill="none" stroke="#fff" stroke-width="1.5"><rect x="2" y="5" width="20" height="14"/><path d="M2 5l10 8 10-8M2 19l7-7M22 19l-7-7"/></svg>
        dkeswick@tidewellhomecraft.co.nz
      </li>
      <li class="web">
        <svg viewBox="0 0 24 24" fill="none" stroke="#fff" stroke-width="1.5"><circle cx="12" cy="12" r="9"/><ellipse cx="12" cy="12" rx="4" ry="9"/><path d="M3 12h18M5 7h14M5 17h14"/></svg>
        tidewellhomecraft.co.nz
      </li>
    </ul>
    <p class="tagline">• tidewell homecraft • solutions for everyone • tidewell homecraft • solutions for everyone •</p>
  </section>

</main>
</body>
</html>
```